Asset Mgmt Firm Business Card Design Project

We need a new business card design for our asset management firm. The name of the firm is Layered MarinCapital, and the firm is referred to as LMC. We would like to see designs that use blues and greys the business card is to be one-sided. The final design should be conservative to communicate financial safety and growth.

The card must include all of the elements below:

Donovan T. Whitlock, PhD MBA
Founding Principal

Layered MarinCapital Inc
418 Harlow Street
New York, NY 10274
212-864-3071
dtwhitlock@layeredmarincapital.example
www.layeredmarincapital.example

Our tagline:
"Weighing steady returns for the long road of life sciences"

Our logo (fiiles attached)

When designing the business card, please abide by Quillmark Press's guidelines here: http://www.quillmarkpress.example/qp/ns/propath/UploadResources.aspx?selectedTab=0?pfid=088&pf_id=088&xnav=DocSpecs#Bleed

Please use Adobe Illustrator or Adobe Photoshop.
Updates

This project has now beenĀ guaranteed.

Best Regards,
Don

Industry/Entity Type

Asset Management

Requirements
Must have
• logo

white background

```html
<!DOCTYPE html>
<html lang="en">
<head>
<meta charset="utf-8">
<title>Layered MarinCapital – Business Card</title>
<link href="https://fonts.googleapis.com/css2?family=Source+Sans+3:wght@400;600&display=swap" rel="stylesheet">
<style>
  :root {
    --page-bg: #f4f4f4;
    --card-grey-light: #c6c6c8;
    --card-grey-mid: #b4b4b7;
    --card-grey-dark: #9d9da0;
    --navy: #1c1f86;
    --ink: #1d1d1d;
    --ink-soft: #2c2c2c;
    --band-white: #f2f2f2;
    --edge-white: #ffffff;
  }
  * { margin: 0; padding: 0; box-sizing: border-box; }
  html, body {
    width: 1200px; height: 900px; overflow: hidden;
    background: var(--page-bg);
    font-family: "Source Sans 3", "Myriad Pro", sans-serif;
  }
  .business-card {
    position: absolute; left: 110px; top: 170px;
    width: 980px; height: 560px;
    overflow: hidden;
    box-shadow: 0 6px 20px rgba(0,0,0,0.18);
  }
  .card-texture {
    position: absolute; inset: 0;
    background: linear-gradient(135deg, var(--card-grey-light) 0%, var(--card-grey-mid) 55%, var(--card-grey-dark) 100%);
  }
  .brand {
    position: absolute; left: 48px; top: 52px;
    display: flex; align-items: center; gap: 20px;
  }
  .brand-mark {
    width: 66px; height: 66px; border-radius: 50%;
    border: 5px solid var(--navy);
  }
  .brand-name {
    font-size: 84px; font-weight: 400; line-height: 1;
    letter-spacing: 8px; color: var(--navy);
  }
  .tagline-band {
    position: absolute; left: 0; top: 176px;
    width: 790px; height: 48px;
    background: var(--band-white);
    display: flex; align-items: center; padding-left: 24px;
    font-size: 30px; color: var(--ink);
    white-space: nowrap;
  }
  .contact-block {
    position: absolute; left: 30px; top: 238px;
    color: var(--ink-soft);
  }
  .person-name { font-size: 36px; font-weight: 600; color: var(--ink); line-height: 44px; }
  .person-title { font-size: 28px; line-height: 36px; margin-bottom: 10px; }
  .contact-line { font-size: 26px; line-height: 31px; white-space: nowrap; }
  .footer-rule {
    position: absolute; left: 0; right: 0; top: 524px; height: 6px;
    background: var(--edge-white);
  }
  .footer-band {
    position: absolute; left: 0; right: 0; top: 530px; height: 22px;
    background: var(--navy);
  }
  .footer-edge {
    position: absolute; left: 0; right: 0; top: 552px; height: 8px;
    background: var(--edge-white);
  }
</style>
</head>
<body>
  <section class="business-card">
    <div class="card-texture" role="img" aria-label="Grey halftone dot texture background"></div>

    <header class="brand">
      <span class="brand-mark"></span>
      <span class="brand-name">LMC</span>
    </header>

    <p class="tagline-band">Weighing steady returns for the long road of life sciences</p>

    <div class="contact-block">
      <p class="person-name">Donovan T. Whitlock, PhD MBA</p>
      <p class="person-title">Founding Principal</p>
      <p class="contact-line">212-864-3071</p>
      <p class="contact-line">www.layeredmarincapital.example</p>
      <p class="contact-line">dtwhitlock@layeredmarincapital.example</p>
      <p class="contact-line">Layered MarinCapital Inc</p>
      <p class="contact-line">418 Harlow Street</p>
      <p class="contact-line">New York, NY 10274</p>
    </div>

    <div class="footer-rule"></div>
    <div class="footer-band"></div>
    <div class="footer-edge"></div>
  </section>
</body>
</html>
```